Business Card Design

We like to use greens as you will see in our logo (but not TOO much green). We are a Dental Clinic in a somewhat eccentric community. We do not like the dated sharp designs which we see many dentists use. We're looking for something bright and fresh while still maintaining the integrity of the profession. Elegance is not necessarily what we are going for... we need for the design to be "mature" but also up-lifting.

See our logo.
Updates

Project Deadline Extended
Reason: We have 5 designs which we like. But we'd like to see a few more before committing to a design.

Project Deadline Extended
Reason: We are awaiting revisions to this project. We are still welcoming designs while we wait to see if designers are able to provide to us the revisions we require in order to proceed with a selection.

Target Market(s)

Younger families - ages late 20's to early 40's

Industry/Entity Type

Business

Contact Information for Business Card

Marlow T. Benning DDS 2740 W. Hollister Rd. Ste. 7 Royal Oak, MI 48133 (248)555-0193 FX (248)555-0147 info@BrightwellDentalCareMi.example BrigthwellDentalCareMi.example on the back of the card we need an appointment reminder (For____ Date___ Time____) with "If you are unable to keep your appointment, kindly give 48 hours notice" at the bottom. No use of teeth in the design. DOUBLE SIDED DESIGN

Requirements
Should not have
• The use of pictures of teeth

```html
<!DOCTYPE html>
<html lang="en">
<head>
<meta charset="utf-8">
<title>Brightwell Dental Care – Business Card</title>
<link rel="stylesheet" href="https://fonts.googleapis.com/css2?family=Cinzel:wght@600;700&family=Roboto+Condensed:wght@400;700&display=swap">
<style>
  :root {
    --stage: #2b2b2b;
    --paper: #ffffff;
    --green: #2fa148;
    --green-light: #6cbf44;
    --green-deep: #1d6a3a;
    --ink: #111111;
    --grey: #4a4a4a;
  }
  * { box-sizing: border-box; margin: 0; padding: 0; }
  html, body { width: 1000px; height: 1200px; overflow: hidden; }
  body { background: var(--stage); position: relative; font-family: "Roboto Condensed", Arial, sans-serif; }

  .card { position: absolute; width: 723px; height: 423px; background: var(--paper); overflow: hidden; }
  .card--front { left: 145px; top: 72px; }
  .card--back { left: 139px; top: 637px; }
  .card__shape { position: absolute; inset: 0; width: 100%; height: 100%; }

  .holder { position: absolute; right: 35px; top: 64px; text-align: right; font-family: "Cinzel", Georgia, serif; }
  .holder__name { font-size: 24px; font-weight: 700; color: var(--ink); letter-spacing: .5px; }
  .holder__title { font-size: 19px; font-weight: 700; color: var(--green); margin-top: 2px; }

  .brand { position: absolute; left: 0; right: 0; top: 132px; display: flex; justify-content: center; align-items: center; gap: 12px; }
  .brand__dot { width: 26px; height: 26px; border-radius: 50%; background: var(--green-light); }
  .brand__name { font-family: "Cinzel", Georgia, serif; font-weight: 600; font-size: 38px; color: var(--green-deep); line-height: 1; }

  .contact { position: absolute; display: flex; align-items: center; gap: 10px; color: #fff; font-size: 20px; }
  .contact--left { left: 35px; }
  .contact--right { right: 35px; }
  .contact__icon { width: 27px; height: 27px; flex: none; }

  .reminder { position: absolute; left: 0; right: 0; top: 188px; display: flex; justify-content: center; align-items: flex-end; font-weight: 700; font-size: 20px; color: var(--ink); }
  .reminder__blank { display: inline-block; border-bottom: 1px solid #888; height: 22px; margin: 0 2px; }
  .notice { position: absolute; left: 0; right: 0; top: 240px; text-align: center; font-family: "Cinzel", Georgia, serif; font-weight: 600; font-size: 22px; line-height: 28px; color: var(--green-deep); letter-spacing: .5px; }
  .address { position: absolute; left: 0; right: 0; top: 333px; display: flex; justify-content: center; align-items: center; gap: 8px; font-weight: 700; font-size: 18px; color: var(--grey); }
  .address__icon { width: 26px; height: 26px; }
</style>
</head>
<body>

<section class="card card--front" aria-label="Card front">
  <svg class="card__shape" viewBox="0 0 723 423" aria-hidden="true">
    <path d="M0,158 Q361,470 723,158 L723,423 L0,423 Z" fill="var(--green-light)"/>
    <path d="M0,172 Q361,488 723,178 L723,423 L0,423 Z" fill="var(--green)"/>
  </svg>
  <div class="holder">
    <div class="holder__name">Marlow T. Benning</div>
    <div class="holder__title">DDS</div>
  </div>
  <div class="brand">
    <span class="brand__dot"></span>
    <span class="brand__name">Brightwell Dental Care</span>
  </div>
  <div class="contact contact--left" style="top:319px">
    <svg class="contact__icon" viewBox="0 0 24 24"><circle cx="12" cy="12" r="12" fill="#fff"/><path d="M8.5 6.5l2 2.2-1.2 1.6c.8 1.7 2 2.9 3.6 3.7l1.6-1.2 2.2 2-1 1.7c-4.2-.3-8.1-4.2-8.3-8.4z" fill="var(--green)"/></svg>
    <span>(248)555-0193</span>
  </div>
  <div class="contact contact--left" style="top:356px">
    <svg class="contact__icon" viewBox="0 0 24 24"><circle cx="12" cy="12" r="12" fill="#fff"/><rect x="6" y="8" width="12" height="8.5" fill="var(--green)"/><path d="M6 8l6 5 6-5" stroke="#fff" stroke-width="1.2" fill="none"/></svg>
    <span>info@BrightwellDentalCareMi.example</span>
  </div>
  <div class="contact contact--right" style="top:319px">
    <span>(248)555-0147</span>
    <svg class="contact__icon" viewBox="0 0 24 24"><circle cx="12" cy="12" r="12" fill="#fff"/><rect x="8" y="6" width="8" height="4" fill="var(--green)"/><rect x="6" y="10.5" width="12" height="5" fill="var(--green)"/><rect x="8" y="14" width="8" height="4" fill="var(--green)" stroke="#fff" stroke-width="1"/></svg>
  </div>
  <div class="contact contact--right" style="top:356px">
    <span>BrigthwellDentalCareMi.example</span>
    <svg class="contact__icon" viewBox="0 0 24 24"><circle cx="12" cy="12" r="12" fill="#fff"/><circle cx="12" cy="12" r="6.5" fill="none" stroke="var(--green)" stroke-width="1.6"/><path d="M5.5 12h13M12 5.5c-2.5 2-2.5 11 0 13M12 5.5c2.5 2 2.5 11 0 13" stroke="var(--green)" stroke-width="1.2" fill="none"/></svg>
  </div>
</section>

<section class="card card--back" aria-label="Card back">
  <svg class="card__shape" viewBox="0 0 723 423" aria-hidden="true">
    <rect width="723" height="423" fill="var(--green)"/>
    <path d="M0,202 Q361,-110 723,190 L723,423 L0,423 Z" fill="var(--green-light)"/>
    <path d="M0,218 Q361,-90 723,212 L723,423 L0,423 Z" fill="var(--paper)"/>
    <circle cx="578" cy="104" r="63" fill="var(--green-light)" stroke="#fff" stroke-width="4"/>
  </svg>
  <div class="reminder">
    <span>(For</span><span class="reminder__blank" style="width:200px"></span>
    <span>Date:</span><span class="reminder__blank" style="width:157px"></span>
    <span>Time:</span><span class="reminder__blank" style="width:92px"></span>
    <span>)</span>
  </div>
  <p class="notice">If you are unable to keep your appointment,<br>kindly give 48 hours notice</p>
  <div class="address">
    <svg class="address__icon" viewBox="0 0 24 24"><circle cx="12" cy="12" r="12" fill="var(--green)"/><path d="M12 5a4.5 4.5 0 0 0-4.5 4.5c0 3.3 4.5 8.5 4.5 8.5s4.5-5.2 4.5-8.5A4.5 4.5 0 0 0 12 5z" fill="#fff"/><circle cx="12" cy="9.5" r="1.7" fill="var(--green)"/></svg>
    <span>2740 W. Hollister Rd. Ste. 7 Royal Oak, MI 48133</span>
  </div>
</section>

</body>
</html>
```